Attorney Website Design

I need a top quality attorney website layout designed. Here are some examples of what I feel are great websites:
http://www.brelmoradivorceattorney.example/
http://www.vethomirlawfirm.example/
http://www.plexfirm.example/
http://www.harrowgatecriminaldefensefirm.example/
http://www.qzfirm.example/
http://www.tolvermoorcriminaldefensefirm.example/
http://www.drennocriminalattorneys.example/
http://www.qzfirm.example/
What we like about these sites:
• The different layers
• Subtle designs, textures, curves
• 3 dimensional
• Floating effects
• Prominent phone number
• Location of Areas of Practice
• Request A Consultation Prominent
• Right side bar with practice areas
• Badges
• Clear Calls to Action
• Dynamic/Staying Top navigation when you scroll
The project will be for a home page and then also an interior page (should be similar to home page).
I want to make it understood I am looking for a design which is not a typical "template" site which I can find anywhere for $50. This budget and project is for a "Custom" website design. Please submit designs similar in quality to the samples links I have posted. Creativity is a MUST! The best way to explain this is, I want a design that I can feel it unique and original, not something that looks like 95% of all websites out there.
Owen
I just wanted everyone to know that so far I am not to pleased with any of the designs. I am not looking for cut/pasting of other peoples websites but ORIGINAL and CREATIVE work.
Industry/Entity Type
Attorney

```html
<!DOCTYPE html>
<html lang="en">
<head>
<meta charset="utf-8">
<title>Tolmer Vale Attorneys</title>
<link rel="stylesheet" href="https://fonts.googleapis.com/css2?family=Open+Sans:ital,wght@0,400;0,600;0,700;1,400&family=Roboto:ital,wght@0,400;0,500;0,700;0,900;1,400;1,500&display=swap">
<style>
:root{
  --navy:#163a66;
  --navy-deep:#0f2c52;
  --slate:#3c5878;
  --gold:#c49a22;
  --gold-light:#dcb546;
  --gold-dark:#a87f12;
  --ink:#2b2b2b;
  --muted:#555;
  --cream:#efe6d2;
  --paper:#f7f2e6;
  --white:#fff;
  --line:#d6d6d6;
}
*{box-sizing:border-box;margin:0;padding:0}
html,body{width:1200px;height:3098px;overflow:hidden}
body{position:relative;background:var(--white);font-family:"Open Sans",Arial,sans-serif;color:var(--ink)}
.abs{position:absolute}
p{font-size:12.5px;line-height:22px;color:var(--muted)}
/* header */
.site-header{left:0;top:0;width:1200px;height:107px;background:linear-gradient(#fdfdfd,#e9ebee);border-top:5px solid var(--navy)}
.brand{left:143px;top:14px;font-family:"Open Sans",sans-serif;font-weight:600;font-size:38px;line-height:40px;color:var(--navy)}
.consult-btn{left:795px;top:0;width:262px;height:40px;background:var(--slate);color:#fff;font-family:"Roboto",sans-serif;font-size:16px;display:flex;align-items:center;justify-content:center;gap:10px;border-radius:0 0 6px 6px}
.call{left:720px;top:50px;display:flex;align-items:center;gap:10px}
.call small{display:block;font-family:Roboto,sans-serif;font-size:12px;font-weight:500;color:var(--ink)}
.call strong{display:block;font-family:Roboto,sans-serif;font-size:24px;font-weight:500;color:var(--navy);line-height:24px}
.social{left:915px;top:60px;display:flex;gap:9px}
.social span{width:24px;height:24px;border-radius:50%;background:var(--slate)}
.social span:first-child{background:#d9682a}
.main-nav{left:0;top:107px;width:1200px;height:50px;background:linear-gradient(var(--gold-light),var(--gold-dark));display:flex;padding-left:142px}
.main-nav a{font-family:Roboto,sans-serif;font-weight:500;font-size:15px;color:#fff;text-decoration:none;padding:0 20px;display:flex;align-items:center;border-right:1px solid rgba(255,255,255,.35)}
.main-nav a.active{background:var(--slate)}
/* hero */
.hero{left:0;top:157px;width:1200px;height:351px;background:linear-gradient(90deg,#b7c1cc 0%,#7e98b8 30%,#9fbcdc 55%,#e8ecef 75%,#c9ced3 100%)}
.hero-bar{left:0;top:444px;width:1200px;height:64px;background:rgba(40,40,40,.55)}
.hero-title{left:143px;top:450px;font-family:Roboto,sans-serif;font-weight:900;font-size:38px;color:#fff;letter-spacing:.5px}
.hero-btn{left:925px;top:456px;width:146px;height:42px;background:linear-gradient(var(--gold-light),var(--gold-dark));color:#fff;font-family:Roboto,sans-serif;font-weight:700;font-size:15px;display:flex;align-items:center;justify-content:center}
.hero-arrow{top:290px;width:40px;height:70px;background:rgba(255,255,255,.85);display:flex;align-items:center;justify-content:center}
/* headings */
.sec-title{font-family:Roboto,sans-serif;font-size:25px;font-weight:500;color:var(--ink)}
.sec-title em{font-style:normal;color:var(--navy)}
/* welcome */
.welcome-photo{left:142px;top:611px;width:255px;height:145px;background:linear-gradient(135deg,#6b4a2e,#a47b4c 45%,#3b3b45)}
.read-more{left:645px;top:980px;font-size:12.5px;color:var(--navy)}
.specialities{left:142px;top:1053px;width:589px;height:217px;background:var(--slate)}
.spec{top:20px;width:150px;text-align:center;color:#fff;font-family:Roboto,sans-serif;font-weight:700;font-size:17px}
.spec .ic{width:132px;height:132px;border-radius:50%;background:radial-gradient(#fff,#cfd3d8);margin:0 auto 14px;display:flex;align-items:center;justify-content:center;border:4px solid #e5e7ea}
/* sidebar */
.practice{left:758px;top:570px;width:318px;height:698px;border:1px solid var(--line);background:#fff;box-shadow:0 0 6px rgba(0,0,0,.12)}
.practice h2{position:absolute;left:16px;top:14px;font-family:Roboto,sans-serif;font-weight:500;font-size:27px}
.practice h2 em{font-style:normal;color:var(--gold)}
.pa{position:absolute;left:12px;width:292px;height:62px;background:linear-gradient(var(--gold-light),var(--gold-dark));color:#fff;font-family:Roboto,sans-serif;font-weight:700;font-size:17px;line-height:21px;padding:0 14px;display:flex;align-items:center;justify-content:space-between;text-transform:uppercase;box-shadow:2px 3px 4px rgba(0,0,0,.25)}
.pa.on{background:linear-gradient(#6d8bb3,#4c6c96)}
/* video */
.video{left:142px;top:1357px;width:589px;height:301px;background:linear-gradient(135deg,#5b3d2a,#2e2a2c 50%,#7b6a5a)}
.controls{left:142px;top:1634px;width:589px;height:24px;background:#e8e8e8;border-top:1px solid #bbb}
.play{left:410px;top:1467px;width:50px;height:50px;border-radius:50%;background:rgba(255,255,255,.55);display:flex;align-items:center;justify-content:center}
/* form */
.ask{left:756px;top:1313px;width:320px;height:455px;background:#eeeeee}
.ask h3{position:absolute;left:22px;top:10px;font-family:Roboto,sans-serif;font-style:italic;font-weight:400;font-size:26px;color:var(--navy)}
.ask .toll{position:absolute;left:22px;top:47px;font-family:Roboto,sans-serif;font-style:italic;font-size:16px;color:var(--gold)}
.field{position:absolute;left:22px;width:276px;height:34px;background:#fff;border:1px solid #cfcfcf;font-size:11px;color:#777;padding:9px 10px}
.send{position:absolute;left:22px;top:400px;width:126px;height:34px;background:var(--slate);color:#fff;font-family:Roboto,sans-serif;font-weight:700;font-size:15px;display:flex;align-items:center;justify-content:center}
/* testimonials */
.testimonials{left:0;top:1809px;width:1200px;height:413px;background:linear-gradient(90deg,#0f2c52,#284c78 45%,#16375f)}
.testimonials h2{position:absolute;left:142px;top:20px;font-family:Roboto,sans-serif;font-weight:500;font-size:27px;color:#fff}
.t-nav{position:absolute;left:1028px;top:22px;color:#fff;font-size:22px;letter-spacing:8px}
.t-photo{position:absolute;left:140px;width:163px;height:127px;border:3px solid #fff;background:linear-gradient(#dfe4ea,#9aa8b8)}
.t-text{position:absolute;left:340px;width:720px;font-style:italic;font-size:12.5px;line-height:23px;color:#fff}
.t-name{position:absolute;left:960px;width:100px;text-align:right;color:#fff;font-family:Roboto,sans-serif;font-size:16px;font-weight:700;line-height:20px}
.t-name span{display:block;font-weight:400;font-size:13px}
.t-rule{position:absolute;left:310px;top:220px;width:750px;height:1px;background:rgba(255,255,255,.35)}
.quote{position:absolute;font-family:Georgia,serif;font-size:40px;color:rgba(255,255,255,.6);line-height:30px}
/* hire */
.hire{left:0;top:2222px;width:1200px;height:359px;background:linear-gradient(#ece4d0,#e2d5b8)}
.hire h2{position:absolute;left:0;width:1200px;top:28px;text-align:center;font-family:Roboto,sans-serif;font-weight:500;font-size:32px;color:var(--ink)}
.hire p{position:absolute;left:152px;width:896px;text-align:center;color:#333;font-size:13px;line-height:23px}
.action-band{left:0;top:2581px;width:1200px;height:58px;background:linear-gradient(var(--gold-light),var(--gold-dark));color:#fff;font-family:Roboto,sans-serif;font-weight:700;font-style:italic;font-size:31px;text-align:center;line-height:58px}
.cta-zone{left:0;top:2639px;width:1200px;height:153px;background:linear-gradient(#ece4d0,#e4d9c0)}
.cta{top:2672px;width:296px;height:74px;background:var(--slate);border-radius:10px;color:#fff;font-family:Roboto,sans-serif;font-size:19px;line-height:24px;display:flex;align-items:center;gap:16px;padding-left:22px;box-shadow:0 4px 6px rgba(0,0,0,.3);text-transform:uppercase}
/* footer */
.footer{left:0;top:2792px;width:1200px;height:182px;background:var(--navy-deep);color:#fff}
.footer h4{position:absolute;font-family:Roboto,sans-serif;font-weight:500;font-size:21px}
.footer h5{position:absolute;font-family:Roboto,sans-serif;font-weight:700;font-size:16px}
.flinks{position:absolute;font-size:11.5px;line-height:22px}
.faddr{position:absolute;font-size:11.5px;line-height:16px;width:200px;padding-left:22px}
.faddr svg,.fcontact svg{position:absolute;left:0;top:2px}
.fcontact{position:absolute;left:945px;top:72px;font-size:11.5px;line-height:28px}
.fcontact div{position:relative;padding-left:26px}
.legal{left:0;top:2974px;width:1200px;height:124px;background:#e8dfc9;text-align:center;font-size:12px;line-height:20px;color:#333}
.legal .fs{display:inline-flex;gap:6px;vertical-align:middle;margin-left:30px}
.legal .fs span{width:20px;height:20px;border-radius:50%;background:#8d8d8d;display:inline-block}
</style>
</head>
<body>

<header class="abs site-header">
  <div class="abs brand" style="left:143px;top:9px">Tolmer Vale<br>Attorneys</div>
</header>
<div class="abs consult-btn">
  <svg width="20" height="14" viewBox="0 0 20 14"><rect x="1" y="1" width="18" height="12" fill="none" stroke="#fff" stroke-width="1.6"/><path d="M1 1l9 7 9-7" fill="none" stroke="#fff" stroke-width="1.6"/></svg>
  Request A Free Consultation
</div>
<div class="abs call">
  <svg width="34" height="34" viewBox="0 0 34 34"><circle cx="17" cy="17" r="16" fill="var(--gold)"/><path d="M11 9c2 0 3 4 2 5l-1 1c1 3 3 5 6 6l1-1c1-1 5 0 5 2s-2 3-4 3c-6 0-12-6-12-12 0-2 1-4 3-4z" fill="#fff"/></svg>
  <div><small>Call Us Today</small><strong>123 456 7890</strong></div>
</div>
<div class="abs social"><span></span><span></span><span></span><span></span></div>

<nav class="abs main-nav">
  <a class="active">Home</a><a>Attorneys &amp; Staff</a><a>Practice Areas</a><a>Testimonials</a><a>Video Center</a><a>About Us</a><a>Contact Us</a>
</nav>

<section class="abs hero" role="img" aria-label="Two smiling attorneys in front of a columned courthouse under a blue sky"></section>
<div class="abs hero-bar"></div>
<div class="abs hero-title">ATTORNEYS YOU CAN TRUST</div>
<div class="abs hero-btn">LEARN MORE</div>
<div class="abs hero-arrow" style="left:0;border-radius:0 35px 35px 0"><svg width="12" height="20"><path d="M10 2L2 10l8 8" stroke="#444" stroke-width="2.5" fill="none"/></svg></div>
<div class="abs hero-arrow" style="left:1160px;border-radius:35px 0 0 35px"><svg width="12" height="20"><path d="M2 2l8 8-8 8" stroke="#444" stroke-width="2.5" fill="none"/></svg></div>

<!-- welcome -->
<h2 class="abs sec-title" style="left:142px;top:566px">Welcome to <em>Tolmer Vale Attorneys</em></h2>
<div class="abs welcome-photo" role="img" aria-label="Attorney meeting a client at a desk in front of a bookcase"></div>
<p class="abs" style="left:414px;top:607px;width:318px">Lorem ipsum dolor sit amet, consectetuer adipiscing elit, sed diam nonummy nibh euismod tincidunt ut laoreet dolore magna aliquam erat volutpat. Ut wisi enim ad minim veniam, quis nostrud exerci tation ullamcorper suscipit lobortis nisl ut aliquip ex ea commodo consequat.Lorem ipsum dolor sit amet,</p>
<p class="abs" style="left:142px;top:739px;width:590px">consectetuer adipiscing elit, sed diam nonummy nibh euismod tincidunt ut laoreet dolore magna aliquam erat volutpat. Ut wisi enim ad minim.Lorem ipsum dolor sit amet, consectetuer adipiscing elit, sed diam nonummy nibh euismod tincidunt ut laoreet dolore magna aliquam erat volutpat. Ut wisi enim ad minim. Lorem ipsum dolor sit amet, consectetuer adipiscing elit, sed diam nonummy nibh euismod tincidunt ut laoreet dolore magna aliquam erat volutpat. Ut wisi enim ad minim.</p>
<p class="abs" style="left:142px;top:893px;width:590px">Lorem ipsum dolor sit amet, consectetuer adipiscing elit, sed diam nonummy nibh euismod tincidunt ut laoreet dolore magna aliquam erat volutpat. Ut wisi enim ad minim.Lorem ipsum dolor sit amet, consectetuer adipiscing elit, sed diam nonummy nibh euismod tincidunt ut laoreet dolore magna aliquam erat volutpat. Ut wisi enim ad minim.</p>
<div class="abs read-more" style="left:645px">Read More &gt;&gt;</div>

<h2 class="abs sec-title" style="left:142px;top:1012px">Our <em>Specialities</em></h2>
<div class="abs specialities">
  <div class="abs spec" style="left:18px">
    <div class="ic"><svg width="70" height="70" viewBox="0 0 70 70" fill="none" stroke="#222" stroke-width="3"><path d="M35 8v52M20 60h30M12 18h46"/><path d="M12 18L4 38h16zM58 18l-8 20h16z"/><path d="M4 38a8 5 0 0016 0M50 38a8 5 0 0016 0" fill="#222"/></svg></div>Criminal Defense</div>
  <div class="abs spec" style="left:220px">
    <div class="ic"><svg width="70" height="70" viewBox="0 0 70 70" fill="#222"><circle cx="22" cy="14" r="6"/><circle cx="48" cy="14" r="6"/><circle cx="35" cy="34" r="4"/><rect x="15" y="23" width="14" height="22" rx="3"/><path d="M41 23h14l4 22H37z"/><rect x="17" y="45" width="4" height="17"/><rect x="23" y="45" width="4" height="17"/><rect x="43" y="45" width="4" height="17"/><rect x="49" y="45" width="4" height="17"/><rect x="31" y="40" width="8" height="12" rx="2"/></svg></div>Family Law</div>
  <div class="abs spec" style="left:420px">
    <div class="ic"><svg width="70" height="70" viewBox="0 0 70 70" fill="none" stroke="#222" stroke-width="3"><rect x="6" y="16" width="58" height="40" rx="3"/><rect x="28" y="10" width="14" height="10" fill="#222"/><circle cx="22" cy="34" r="6" fill="#222"/><path d="M12 50c2-8 18-8 20 0" fill="#222"/><path d="M38 30h18M38 38h18M38 46h12"/></svg></div>Personal Injury</div>
</div>

<!-- practice areas -->
<aside class="abs practice">
  <h2>Practice <em>Areas</em></h2>
  <div class="pa on" style="top:66px">DUI Defense<svg width="24" height="24"><circle cx="12" cy="12" r="11" fill="#fff"/><path d="M6 12l4 4 8-8" stroke="#4c6c96" stroke-width="2.6" fill="none"/></svg></div>
  <div class="pa" style="top:145px">Serious Vehicular<br>Crimes<svg width="24" height="24"><circle cx="12" cy="12" r="10.5" fill="none" stroke="#fff" stroke-width="2"/><path d="M12 6v12M6 12h12" stroke="#fff" stroke-width="2.4"/></svg></div>
  <div class="pa" style="top:224px">Theft Crimes<svg width="24" height="24"><circle cx="12" cy="12" r="10.5" fill="none" stroke="#fff" stroke-width="2"/><path d="M12 6v12M6 12h12" stroke="#fff" stroke-width="2.4"/></svg></div>
  <div class="pa" style="top:303px">Drug Crimes<svg width="24" height="24"><circle cx="12" cy="12" r="10.5" fill="none" stroke="#fff" stroke-width="2"/><path d="M12 6v12M6 12h12" stroke="#fff" stroke-width="2.4"/></svg></div>
  <div class="pa" style="top:382px">Sex Crimes<svg width="24" height="24"><circle cx="12" cy="12" r="10.5" fill="none" stroke="#fff" stroke-width="2"/><path d="M12 6v12M6 12h12" stroke="#fff" stroke-width="2.4"/></svg></div>
  <div class="pa" style="top:461px">High School and<br>College Cases<svg width="24" height="24"><circle cx="12" cy="12" r="10.5" fill="none" stroke="#fff" stroke-width="2"/><path d="M12 6v12M6 12h12" stroke="#fff" stroke-width="2.4"/></svg></div>
  <div class="pa" style="top:540px">Other Offenses<svg width="24" height="24"><circle cx="12" cy="12" r="10.5" fill="none" stroke="#fff" stroke-width="2"/><path d="M12 6v12M6 12h12" stroke="#fff" stroke-width="2.4"/></svg></div>
  <div class="pa" style="top:619px">Expungement<svg width="24" height="24"><circle cx="12" cy="12" r="10.5" fill="none" stroke="#fff" stroke-width="2"/><path d="M12 6v12M6 12h12" stroke="#fff" stroke-width="2.4"/></svg></div>
</aside>

<!-- video -->
<h2 class="abs sec-title" style="left:142px;top:1306px">Our <em>Video</em></h2>
<div class="abs video" role="img" aria-label="Video still of attorneys and clients meeting around a conference table"></div>
<div class="abs play"><svg width="20" height="22"><path d="M4 2l14 9-14 9z" fill="#fff"/></svg></div>
<div class="abs controls">
  <svg width="589" height="24" style="position:absolute;left:0;top:0"><path d="M8 7l8 5-8 5z" fill="#333"/><text x="30" y="16" font-size="10" font-family="Open Sans" fill="#333">00:00</text><rect x="70" y="10" width="380" height="4" fill="#999"/><text x="460" y="16" font-size="10" font-family="Open Sans" fill="#333">00:00</text><path d="M505 9h4l5-4v14l-5-4h-4z" fill="#333"/><rect x="520" y="10" width="30" height="4" fill="#555"/><path d="M565 7h6M565 7v6M581 17h-6M581 17v-6" stroke="#333" stroke-width="2" fill="none"/></svg>
</div>
<p class="abs" style="left:142px;top:1674px;width:590px">Lorem ipsum dolor sit amet, consectetuer adipiscing elit, sed diam nonummy nibh euismod tincidunt ut laoreet dolore magna aliquam erat volutpat. Lorem ipsum dolor sit amet, consectetuer adipiscing elit, sed diam nonummy nibh euismod tincidunt ut laoreet dolore magna aliquam erat volutpat.</p>

<!-- ask form -->
<aside class="abs ask">
  <h3>Ask Us Question?</h3>
  <div class="toll">TOLL FREE : 1 (800) 555-0142</div>
  <div class="field" style="top:80px">Enter your First Name</div>
  <div class="field" style="top:131px">Enter your Last Name</div>
  <div class="field" style="top:182px">Enter your Email Address</div>
  <div class="field" style="top:233px">Enter your Phone Number</div>
  <div class="field" style="top:284px;height:100px">Enter your Message</div>
  <div class="send">SEND NOW</div>
</aside>

<!-- testimonials -->
<section class="abs testimonials">
  <h2>Client Testimonials</h2>
  <div class="t-nav">&lsaquo;&rsaquo;</div>
  <div class="t-photo" style="top:71px" role="img" aria-label="Portrait of a smiling female client"></div>
  <div class="quote" style="left:312px;top:66px">&ldquo;</div>
  <div class="t-text" style="top:68px">Lorem ipsum dolor sit amet, consectetuer adipiscing elit, sed diam nonummy nibh euismod tincidunt ut laoreet dolore magna aliquam erat volutpat. Lorem ipsum dolor sit amet, consectetuer adipiscing elit, sed diam nonummy nibh euismod tincidunt ut laoreet dolore magna aliquam erat volutpat. Lorem ipsum dolor sit amet, consectetuer adipiscing elit, sed diam nonummy nibh euismod tincidunt ut laoreet dolore magna aliquam erat volutpat.</div>
  <div class="quote" style="left:888px;top:150px">&rdquo;</div>
  <div class="t-name" style="top:168px">Lorem ipsum<span>Lorem ipsum</span></div>
  <div class="t-rule"></div>
  <div class="t-photo" style="top:244px" role="img" aria-label="Portrait of a smiling male client in a suit"></div>
  <div class="quote" style="left:312px;top:238px">&ldquo;</div>
  <div class="t-text" style="top:240px">Lorem ipsum dolor sit amet, consectetuer adipiscing elit, sed diam nonummy nibh euismod tincidunt ut laoreet dolore magna aliquam erat volutpat. Lorem ipsum dolor sit amet, consectetuer adipiscing elit, sed diam nonummy nibh euismod tincidunt ut laoreet dolore magna aliquam erat volutpat. Lorem ipsum dolor sit amet, consectetuer adipiscing elit, sed diam nonummy nibh euismod tincidunt ut laoreet dolore magna aliquam erat volutpat.</div>
  <div class="quote" style="left:888px;top:322px">&rdquo;</div>
  <div class="t-name" style="top:340px">Lorem ipsum<span>Lorem ipsum</span></div>
</section>

<!-- hire -->
<section class="abs hire">
  <h2>Should I Hire A Tolmer Vale Attorneys As Defense Lawyer?</h2>
  <p style="top:94px">When a person is arrested or is under investigation for a criminal offense of some sort, it can be difficult to know what to do. The arresting officer or other law enforcement personnel may have told you that there is no hope of avoiding a conviction. The criminal charges you face may be so serious that you feel there's no way to avoid years or even life in prison. It is important to remember that you always have options. With a competent criminal lawyer at your side, you can fight your charges and seek a just outcome.</p>
  <p style="top:210px">Our attorneys can fully investigate your case in order to determine what can be done to protect your rights. You can trust that we can work to gather evidence and witness testimony on your behalf and develop a strategy that utilizes the legal system in your favor. Just because you have been arrested does not mean that you have lost your rights. In fact, you are granted the right to legal counsel under the U.S. Constitution. By exercising this right, you have the opportunity to effectively avoid maximum penalties or a conviction.</p>
</section>
<div class="abs action-band">What Would You Like To Do Now?</div>
<div class="abs cta-zone"></div>
<div class="abs cta" style="left:142px"><svg width="44" height="44" viewBox="0 0 44 44" fill="none" stroke="#fff" stroke-width="2.4"><rect x="10" y="10" width="24" height="24" transform="rotate(45 22 22)"/><circle cx="22" cy="22" r="5"/></svg><span>Learn More About<br>Criminal Defense</span></div>
<div class="abs cta" style="left:455px"><svg width="44" height="44" viewBox="0 0 44 44" fill="none" stroke="#fff" stroke-width="2.4"><rect x="8" y="6" width="26" height="34" rx="2"/><path d="M15 4h12v6H15zM13 20l3 3 5-6M13 31l3 3 5-6M25 21h6M25 32h6"/></svg><span>Get A Free Case<br>Evaluation</span></div>
<div class="abs cta" style="left:770px"><svg width="44" height="44" viewBox="0 0 44 44" fill="#fff"><circle cx="22" cy="13" r="8"/><path d="M6 42c0-12 7-18 16-18s16 6 16 18z"/></svg><span>Learn About The<br>Attorneys</span></div>

<!-- footer -->
<footer class="abs footer">
  <h4 style="left:142px;top:24px">Quick Links</h4>
  <div class="flinks" style="left:142px;top:66px">&gt; Home<br>&gt;Attorneys &amp; Staff<br>&gt; Practice Areas<br>&gt;Testimonials</div>
  <div class="flinks" style="left:276px;top:66px">&gt; Video Center<br>&gt; Free Consultation<br>&gt; About Us<br>&gt; Contact Us</div>
  <h4 style="left:428px;top:24px">Our Locations</h4>
  <h5 style="left:428px;top:66px">Main Office:</h5>
  <div class="faddr" style="left:428px;top:100px"><svg width="12" height="16"><path d="M6 1a5 5 0 015 5c0 4-5 9-5 9S1 10 1 6a5 5 0 015-5z" fill="#fff"/><circle cx="6" cy="6" r="2" fill="var(--navy-deep)"/></svg>Lorem ipsum dolor sit amet consectetuer adipiscing elit Lorem ipsum dolor sit amet, consectetue</div>
  <h5 style="left:688px;top:66px">Ocala Office:</h5>
  <div class="faddr" style="left:688px;top:100px"><svg width="12" height="16"><path d="M6 1a5 5 0 015 5c0 4-5 9-5 9S1 10 1 6a5 5 0 015-5z" fill="#fff"/><circle cx="6" cy="6" r="2" fill="var(--navy-deep)"/></svg>Lorem ipsum dolor sit amet consectetuer adipiscing elit Lorem ipsum dolor sit amet, consectetue</div>
  <div class="fcontact">
    <div><svg width="16" height="14"><rect x="1" y="4" width="14" height="9" rx="1" fill="#fff"/><rect x="4" y="1" width="8" height="4" fill="#fff"/></svg>123-456-7890</div>
    <div><svg width="16" height="16"><path d="M4 2c2 0 3 3 2 4l-1 1c1 2 2 3 4 4l1-1c1-1 4 0 4 2s-2 2-3 2C6 14 2 10 2 5c0-2 1-3 2-3z" fill="#fff"/></svg>123-456-7890</div>
    <div><svg width="16" height="12"><rect x="1" y="1" width="14" height="10" fill="#fff"/><path d="M1 1l7 5 7-5" stroke="var(--navy-deep)" stroke-width="1.4" fill="none"/></svg>info@tolmervale.example</div>
  </div>
</footer>
<div class="abs legal">
  <div style="padding-top:20px">The information on this website is for general information purposes only. Nothing on this site should be taken as legal advice for any individual<br>case or situation. This information is not intended to create, and receipt or viewing does not constitute, an attorney-client relationship.</div>
  <div style="margin-top:18px">Copyright &copy; 2014 TolmerValeAttorneys.example. All Rights Reserved. I Privacy Policy <span class="fs"><span></span><span></span><span></span><span></span></span></div>
</div>

</body>
</html>
```